Tidyvale- Home Organization and Staging Company needs Logo and Business Cards

I would like eclectic, but classy business card design for my Home Organization/Home Staging business. I would really like to incorporate a little princess crown “cocked“ to the left side of hanger to I am also going to order some post card flyers very soon. As quickly as I can figure out what exact information I want on it.

Target Market(s)

Realtors, Homeowners, Interior Designers

Contact Information for Business Card

Marla Penwick
Owner/Consultant
Phone -(919) 555-0173
Email- Marlapw382@brightmail.example
Website- www.Tidyvale.example

Font styles to use
Script

Colors
e34197
e667a6
eea4c8

Requirements
Nice to have
• Please try add a little piano chair under the house. See updates photos below for example.

```html
<!DOCTYPE html>
<html lang="en">
<head>
<meta charset="utf-8">
<title>Tidyvale – Business Cards</title>
<link rel="stylesheet" href="https://fonts.googleapis.com/css2?family=Open+Sans:wght@400;600&family=Quicksand:wght@300;500&display=swap">
<style>
  :root {
    --stage: #8a8a8a;
    --stage-light: #a3a3a3;
    --card-front: #f6dde8;
    --card-back: #d6739c;
    --brand-pink: #d9689c;
    --brand-deep: #e34197;
    --ink: #4d4d4d;
    --white: #ffffff;
    --tag-light: #f9e3ee;
  }
  * { box-sizing: border-box; margin: 0; padding: 0; }
  html, body { width: 1200px; height: 900px; overflow: hidden; }
  body {
    background: radial-gradient(ellipse at 50% 40%, var(--stage-light), var(--stage));
    position: relative;
    font-family: "Open Sans", sans-serif;
  }
  .card {
    position: absolute;
    width: 520px;
    height: 297px;
    border-radius: 22px;
    box-shadow: 0 6px 18px rgba(0,0,0,0.25);
    overflow: hidden;
  }
  .card--front { left: 50px; top: 150px; background: var(--card-front); }
  .card--back { left: 630px; top: 150px; background: var(--card-back); }

  .brand-name {
    font-family: "Quicksand", sans-serif;
    font-weight: 500;
    letter-spacing: 1px;
    display: block;
    text-align: center;
  }
  .card--front .brand-name { color: var(--brand-pink); font-size: 40px; margin-top: 40px; }
  .card--back .brand-name { color: var(--white); font-size: 46px; margin-top: 86px; }

  .holder { text-align: center; margin-top: 14px; }
  .holder-name {
    font-size: 21px;
    letter-spacing: 2.5px;
    color: var(--ink);
    text-transform: uppercase;
    font-weight: 400;
  }
  .holder-role {
    font-size: 12px;
    letter-spacing: 1.5px;
    color: var(--brand-pink);
    text-transform: uppercase;
    font-weight: 600;
    margin-top: 2px;
  }

  .contact-list {
    position: absolute;
    left: 34px;
    bottom: 24px;
    list-style: none;
  }
  .contact-item {
    display: flex;
    align-items: center;
    gap: 9px;
    font-size: 14px;
    font-weight: 600;
    color: var(--ink);
    line-height: 24px;
  }
  .contact-item svg { width: 14px; height: 14px; flex: none; }

  .tagline {
    font-family: "Quicksand", sans-serif;
    font-weight: 300;
    text-align: center;
    letter-spacing: 0.5px;
  }
  .card--back .tagline { color: var(--tag-light); font-size: 20px; margin-top: 14px; }

  .lockup {
    position: absolute;
    left: 0;
    right: 0;
    top: 600px;
    text-align: center;
  }
  .lockup .brand-name { color: var(--brand-pink); font-size: 62px; }
  .lockup .tagline { color: var(--brand-pink); font-size: 26px; margin-top: 12px; }
</style>
</head>
<body>

  <section class="card card--front" aria-label="Business card front">
    <span class="brand-name">Tidyvale</span>
    <div class="holder">
      <p class="holder-name">Marla Penwick</p>
      <p class="holder-role">Owner/Consultant</p>
    </div>
    <ul class="contact-list">
      <li class="contact-item">
        <svg viewBox="0 0 16 16" aria-hidden="true"><path fill="#d9689c" d="M3.5 1.5l2.5 0 1 3.5-1.6 1.2a8 8 0 0 0 4.4 4.4L11 9l3.5 1v2.5c0 1-1 1.8-2 1.7C6.5 13.6 2.4 9.5 1.8 3.5c-.1-1 .7-2 1.7-2z"/></svg>
        (919) 555-0173
      </li>
      <li class="contact-item">
        <svg viewBox="0 0 16 16" aria-hidden="true"><rect x="1" y="3" width="14" height="10" rx="1" fill="#d9689c"/><path d="M1.5 3.8L8 9l6.5-5.2" stroke="#f6dde8" stroke-width="1.3" fill="none"/></svg>
        Marlapw382@brightmail.example
      </li>
      <li class="contact-item">
        <svg viewBox="0 0 16 16" aria-hidden="true"><circle cx="8" cy="8" r="7" fill="#d9689c"/><path d="M1 8h14M8 1c-2.5 2-2.5 12 0 14M8 1c2.5 2 2.5 12 0 14" stroke="#f6dde8" stroke-width="1" fill="none"/></svg>
        www.Tidyvale.example
      </li>
    </ul>
  </section>

  <section class="card card--back" aria-label="Business card back">
    <span class="brand-name">Tidyvale</span>
    <p class="tagline">Sorted &bull; Organized &bull; Staged</p>
  </section>

  <section class="lockup" aria-label="Brand lockup">
    <span class="brand-name">Tidyvale</span>
    <p class="tagline">Sorted &bull; Organized &bull; Staged</p>
  </section>

</body>
</html>
```